Meridian Handsets business card design

I would like to see some designs for a business card for Meridian Handsets. I would like the business card to be double sided. It will need to have a similar colour / look and feel to our website www.meridianhandsets.com.au I have also attached our latest flyer. Final designs to be handed over in Photoshop format so that I can edit the business card when needed please.

Industry/Entity Type

Business

Contact Information for Business Card

Gavin Thornley
sales@meridianhandsets.com.au
Business Development Manager
ph: (08) 6197 5821
www.meridianhandsets.com.au

Font styles to use
Serif
Sans Serif

Requirements
Must have
• If you could please utilise our colour scheme as seen on our website and the attached flyer.
• I would also like the final design to be in a Photoshop format so that I can edit it when needed please.

```html
<!DOCTYPE html>
<html lang="en">
<head>
<meta charset="utf-8">
<title>Meridian Handsets — Business Card</title>
<link rel="stylesheet" href="https://fonts.googleapis.com/css2?family=Jost:wght@400;500&display=swap">
<style>
  :root {
    --brand-blue: #17509a;
    --brand-blue-light: #2a66b3;
    --brand-blue-deep: #124482;
    --accent-green: #2aa882;
    --accent-green-light: #41c79b;
    --card-silver: #ececec;
    --card-white: #f8f8f8;
    --ink-dark: #2f2f33;
    --ink-grey: #5a5a5e;
    --page-bg: #e6e6e3;
    --white: #ffffff;
  }
  * { box-sizing: border-box; margin: 0; padding: 0; }
  html, body {
    width: 1200px; height: 1200px; overflow: hidden;
    background: var(--page-bg);
    font-family: "Jost", "Futura", Arial, sans-serif;
  }
  .sheet {
    width: 1200px; height: 1200px;
    display: flex; flex-direction: column;
    align-items: center; justify-content: center; gap: 60px;
  }
  .card {
    position: relative;
    width: 900px; height: 514px;
    overflow: hidden;
    box-shadow: 0 10px 30px rgba(0,0,0,0.18);
  }
  /* Back side */
  .card-back {
    background: linear-gradient(135deg, var(--brand-blue-light) 0%, var(--brand-blue) 45%, var(--brand-blue-deep) 100%);
    display: flex; align-items: center; justify-content: center; gap: 22px;
  }
  .card-back .brand-dot {
    width: 34px; height: 34px; border-radius: 50%;
    background: var(--white);
  }
  .card-back .brand-name {
    color: var(--white);
    font-weight: 500;
    font-size: 62px;
    letter-spacing: 0.5px;
  }
  /* Front side */
  .card-front { background: linear-gradient(160deg, var(--card-white) 0%, var(--card-silver) 100%); }
  .card-front .shapes { position: absolute; inset: 0; }
  .card-front .brand-name {
    position: absolute; left: 0; right: 0; top: 88px;
    text-align: center;
    color: var(--ink-dark);
    font-weight: 500;
    font-size: 64px;
    line-height: 1.1;
    letter-spacing: 0.5px;
  }
  .person {
    position: absolute; left: 58px; top: 228px;
  }
  .person .name {
    color: var(--accent-green);
    font-weight: 500;
    font-size: 32px;
    line-height: 38px;
    letter-spacing: 0.5px;
  }
  .person .role {
    color: var(--ink-grey);
    font-weight: 400;
    font-size: 19px;
    line-height: 24px;
    letter-spacing: 0.3px;
  }
  .contact {
    position: absolute; left: 58px; top: 404px;
    list-style: none;
    color: var(--white);
    font-size: 21px; font-weight: 400;
    letter-spacing: 0.3px;
  }
  .contact li { display: flex; align-items: center; gap: 16px; height: 30px; }
  .contact svg { width: 18px; height: 18px; flex: none; }
</style>
</head>
<body>
<main class="sheet">

  <section class="card card-back" aria-label="Business card, back">
    <span class="brand-dot"></span>
    <span class="brand-name">Meridian Handsets</span>
  </section>

  <section class="card card-front" aria-label="Business card, front">
    <svg class="shapes" viewBox="0 0 900 514" width="900" height="514" aria-hidden="true">
      <defs>
        <linearGradient id="blueBand" x1="0" y1="0" x2="1" y2="1">
          <stop offset="0" stop-color="#2a66b3"/>
          <stop offset="1" stop-color="#124482"/>
        </linearGradient>
        <linearGradient id="greenBand" x1="0" y1="0" x2="1" y2="0">
          <stop offset="0" stop-color="#2aa882"/>
          <stop offset="1" stop-color="#41c79b"/>
        </linearGradient>
      </defs>
      <polygon points="0,386 900,234 900,514 0,514" fill="url(#blueBand)"/>
      <polygon points="0,368 436,294 444,307 0,382" fill="url(#greenBand)"/>
    </svg>

    <h1 class="brand-name">Meridian Handsets</h1>

    <div class="person">
      <p class="name">Gavin Thornley</p>
      <p class="role">Business Development Manager</p>
    </div>

    <ul class="contact">
      <li>
        <svg viewBox="0 0 24 24" aria-hidden="true"><path fill="#41c79b" d="M6.6 10.8a15.1 15.1 0 0 0 6.6 6.6l2.2-2.2a1 1 0 0 1 1-.25 11.4 11.4 0 0 0 3.6.57 1 1 0 0 1 1 1V20a1 1 0 0 1-1 1A17 17 0 0 1 3 4a1 1 0 0 1 1-1h3.5a1 1 0 0 1 1 1c0 1.250.2 2.45.57 3.57a1 1 0 0 1-.25 1z"/></svg>
        <span>(08) 6197 5821</span>
      </li>
      <li>
        <svg viewBox="0 0 24 24" aria-hidden="true"><rect x="2" y="5" width="20" height="14" rx="1.5" fill="#41c79b"/><path d="M3 6l9 7 9-7" fill="none" stroke="#17509a" stroke-width="1.6"/></svg>
        <span>sales@meridianhandsets.com.au</span>
      </li>
      <li>
        <svg viewBox="0 0 24 24" aria-hidden="true"><circle cx="12" cy="12" r="10" fill="#41c79b"/><path d="M2 12h20M12 2c3 3 3 17 0 20M12 2c-3 3-3 17 0 20" fill="none" stroke="#17509a" stroke-width="1.4"/></svg>
        <span>www.meridianhandsets.com.au</span>
      </li>
    </ul>
  </section>

</main>
</body>
</html>
```